Corvane Project Services - Flyer

Project Breif:
I need a single page A4 Capability Statement, which will be used to market our services to prospective clients, both in print and via email PDF.
It needs to look professional and should incorporate the elements I have uploaded into files, these include:
Capability Statement Text
Corvane Services Company Logo
Additional Logo’s (Tools We Use)
Glimmer Bay Pics can be cut into the page
I have included examples of capability statements as a guide to what i am looking for.
Regards
Derek
Engineering Consulting

```html
<!DOCTYPE html>
<html lang="en">
<head>
<meta charset="utf-8">
<title>Corvane Project Services – Capability Statement</title>
<link href="https://fonts.googleapis.com/css2?family=Roboto:wght@300;400;500;700&display=swap" rel="stylesheet">
<style>
:root{
  --blue:#4a86c8;
  --blue-text:#3f86cc;
  --ink:#1d1d1d;
  --body:#4a4a4a;
  --dark-tab:#3b3b3b;
  --stage:#e9ecef;
  --paper:#ffffff;
}
*{margin:0;padding:0;box-sizing:border-box}
html,body{width:1162px;height:1200px;overflow:hidden;background:var(--stage);font-family:"Roboto",Arial,sans-serif}
.canvas{position:relative;width:1162px;height:1200px}
.flyer{position:absolute;left:117px;top:0;width:935px;height:1210px;background:var(--paper);transform:scale(.9917);transform-origin:0 0;overflow:hidden}
.flyer-art{position:absolute;left:0;top:0}
.brand{position:absolute;left:44px;top:80px;width:215px;text-align:center;color:var(--ink)}
.brand-mark{display:block;width:56px;height:56px;border-radius:50%;background:var(--blue);margin:0 auto 12px}
.brand-name{font-weight:700;font-size:17px;letter-spacing:.5px;line-height:1.2}
.title-box{position:absolute;left:430px;top:67px;width:449px;height:64px;background:var(--blue);color:#fff;font-weight:300;font-size:42px;line-height:64px;text-align:center}
.intro{position:absolute;left:58px;top:426px;width:320px}
.intro-lead{color:var(--blue-text);font-weight:300;font-size:24px;line-height:29.5px;margin-bottom:22px}
.intro p.body{color:var(--body);font-weight:300;font-size:17.2px;line-height:22px;margin-bottom:22px}
.services{position:absolute;left:477px;top:416px;width:430px}
.services-title{color:var(--blue-text);font-weight:300;font-size:32px;margin-bottom:28px}
.service{position:relative;padding-left:57px;margin-bottom:20px}
.service-icon{position:absolute;left:0;top:-10px;width:38px;height:38px}
.service h3{font-size:17.2px;font-weight:500;color:var(--ink);line-height:22px}
.service ul{list-style:none}
.service li{position:relative;padding-left:30px;color:var(--body);font-weight:300;font-size:17.2px;line-height:22px}
.service li::before{content:"";position:absolute;left:6px;top:8px;width:7px;height:7px;border-radius:50%;background:var(--blue)}
.contact-tab{position:absolute;left:443px;top:1054px;width:191px;height:40px;background:var(--dark-tab);color:#fff;font-size:24px;font-weight:300;line-height:40px;text-align:center}
.contact-list{position:absolute;left:577px;top:1101px;list-style:none;color:#fff;font-size:16.5px;font-weight:300}
.contact-list li{display:flex;align-items:center;height:23px}
.contact-list svg{width:16px;height:16px;margin-right:15px;flex:none}
</style>
</head>
<body>
<div class="canvas">
  <div class="flyer">
    <svg class="flyer-art" width="935" height="1210" viewBox="0 0 935 1210">
      <defs>
        <linearGradient id="deskPhoto" x1="0" y1="0" x2="1" y2="1">
          <stop offset="0" stop-color="#dfe6ee"/>
          <stop offset=".5" stop-color="#f2f4f7"/>
          <stop offset="1" stop-color="#b9cde3"/>
        </linearGradient>
        <linearGradient id="chartPhoto" x1="0" y1="0" x2="1" y2="1">
          <stop offset="0" stop-color="#eef1f6"/>
          <stop offset="1" stop-color="#c9d3e2"/>
        </linearGradient>
      </defs>
      <polygon points="685,0 935,0 935,383 0,383 0,207 600,207" fill="url(#deskPhoto)" role="img" aria-label="Photo: hands reviewing printed documents with pens at a desk"/>
      <polygon points="370,131 430,131 650,131 600,207 440,207" fill="#c9ccd0"/>
      <polygon points="0,970 410,970 515,1210 0,1210" fill="url(#chartPhoto)" role="img" aria-label="Photo: printed project schedule Gantt chart with a pen"/>
      <polygon points="470,1063 935,1063 935,1210 518,1210" fill="var(--blue)"/>
    </svg>

    <div class="brand">
      <span class="brand-mark"></span>
      <div class="brand-name">CORVANE PROJECT SERVICES</div>
    </div>

    <div class="title-box">Capability Statement</div>

    <section class="intro">
      <p class="intro-lead">Corvane Project Services Ltd. is a leading project control consultancy based in Co Cork Ireland</p>
      <p class="body">For over 20 years we have been helping our clients to deliver complex projects and programs throughout mainland Europe.</p>
      <p class="body">We are passionate about empower organisations to achieve their objectives, on time and on budget.</p>
      <p class="body">We are continually innovating, evolving and learning, utilize the latest industry tools and techniques to deliver real value to our clients.</p>
      <p class="body">Our goal is to make successful project delivery more achievable and repeatable.</p>
    </section>

    <section class="services">
      <h2 class="services-title">Core Services:</h2>
      <div class="service">
        <svg class="service-icon" viewBox="0 0 38 38" fill="none" stroke="var(--blue)" stroke-width="1.4">
          <rect x="3" y="6" width="30" height="25" rx="1"/><line x1="3" y1="12" x2="33" y2="12"/>
          <line x1="9" y1="3" x2="9" y2="8"/><line x1="27" y1="3" x2="27" y2="8"/>
          <circle cx="10" cy="18" r="1.5"/><circle cx="18" cy="18" r="1.5"/><circle cx="26" cy="18" r="1.5"/>
          <circle cx="10" cy="25" r="1.5"/><circle cx="18" cy="25" r="1.5"/><path d="M28 34l6-8 2 2-6 8z"/>
        </svg>
        <h3>Planning and Scheduling</h3>
        <ul>
          <li>Tender Planning</li>
          <li>Interactive Planning / Pull Planning</li>
          <li>EPCMV Planning &amp; Scheduling</li>
          <li>Schedule Earned Value Management</li>
          <li>Independent Schedule Quality Assessment</li>
          <li>Schedule Risk Analysis (Monte Carlo) Training</li>
        </ul>
      </div>
      <div class="service">
        <svg class="service-icon" viewBox="0 0 38 38" fill="none" stroke="var(--blue)" stroke-width="1.4">
          <rect x="4" y="4" width="22" height="30" rx="1"/><line x1="9" y1="12" x2="21" y2="12"/>
          <line x1="9" y1="18" x2="21" y2="18"/><line x1="9" y1="24" x2="17" y2="24"/>
          <circle cx="29" cy="25" r="6"/><line x1="29" y1="22" x2="29" y2="26"/><circle cx="29" cy="28" r=".6"/>
        </svg>
        <h3>Management of Risk</h3>
        <ul>
          <li>Risk Management Policies &amp; Procedures</li>
          <li>Risk Management Strategy</li>
          <li>Risk Registers</li>
          <li>Risk Improvement Planning</li>
          <li>Risk Response and Communication</li>
          <li>Risk Management Training</li>
        </ul>
      </div>
      <div class="service">
        <svg class="service-icon" viewBox="0 0 38 38" fill="none" stroke="var(--blue)" stroke-width="1.4">
          <path d="M12 4h10l-3 6h-4z"/><path d="M15 10C5 14 3 30 10 34h14c6-4 4-20-5-24"/>
          <rect x="21" y="20" width="14" height="15" rx="1"/><line x1="24" y1="24" x2="32" y2="24"/>
          <line x1="24" y1="28" x2="32" y2="28"/><line x1="24" y1="32" x2="32" y2="32"/>
        </svg>
        <h3>Cost Control:</h3>
        <ul>
          <li>Estimating &amp; Forecasting</li>
          <li>Earned Value Analysis</li>
          <li>Progress Reporting</li>
          <li>Cost Risk Analysis</li>
        </ul>
      </div>
    </section>

    <div class="contact-tab">Contact Us</div>
    <ul class="contact-list">
      <li><svg viewBox="0 0 16 16" fill="#1d1d1d"><circle cx="8" cy="5" r="3.5"/><path d="M1 16c0-5 3-7 7-7s7 2 7 7z"/></svg>Derek Halloran (Managing Director)</li>
      <li><svg viewBox="0 0 16 16" fill="none" stroke="#1d1d1d" stroke-width="2.2" stroke-linecap="round"><path d="M12 2C6 3 3 8 4 14"/></svg>+353 (0)87 555 0142</li>
      <li><svg viewBox="0 0 16 16" fill="none" stroke="#1d1d1d" stroke-width="1.6"><rect x="2" y="4" width="12" height="8"/><path d="M2 4l6 5 6-5"/></svg>info@corvaneservices.ie</li>
      <li><svg viewBox="0 0 16 16" fill="none" stroke="#1d1d1d" stroke-width="1.4"><circle cx="8" cy="8" r="6"/><ellipse cx="8" cy="8" rx="2.6" ry="6"/><line x1="2" y1="8" x2="14" y2="8"/></svg>www.corvaneservices.ie</li>
    </ul>
  </div>
</div>
</body>
</html>
```